Corvenne Jewelers Business Cards

A creative, cool edgy business card for our entire team that says we are a young, hip, luxury jewelry store specializing in diamonds and engagement rings but that we are also personal shoppers and trusted advisors. Our colors are Navy Blue & Platinum

I have included our past business card.

Font styles to use
Serif

Colors
0255a3

Requirements
Nice to have
• A card stock that you can write on with a pen

```html
<!DOCTYPE html>
<html lang="en">
<head>
<meta charset="utf-8">
<title>Corvenne Jewelers Business Cards</title>
<link rel="stylesheet" href="https://fonts.googleapis.com/css2?family=Cormorant+Garamond:wght@500&family=Tinos:wght@700&family=Open+Sans:wght@400&display=swap">
<style>
  :root {
    --backdrop: #c4c5c7;
    --brand-blue: #0255a3;
    --navy: #262a66;
    --platinum: #e4e4e4;
    --card-white: #ffffff;
    --ink: #1a1a1a;
  }
  html, body {
    margin: 0;
    padding: 0;
    width: 1200px;
    height: 1200px;
    overflow: hidden;
    background: var(--backdrop);
  }
  .canvas {
    position: relative;
    width: 1200px;
    height: 1200px;
  }
  .card {
    position: absolute;
    width: 929px;
    height: 530px;
    border-radius: 36px;
    overflow: hidden;
  }
  .card--front {
    left: 84px;
    top: 35px;
    background: var(--card-white);
  }
  .card--back {
    left: 204px;
    top: 625px;
    background: var(--brand-blue);
  }
  .card__band {
    position: absolute;
    left: 0;
    top: 0;
    width: 929px;
    height: 530px;
  }
  .brand-mark {
    position: absolute;
    left: 122px;
    top: 58px;
  }
  .brand-name {
    position: absolute;
    font-family: "Cormorant Garamond", serif;
    font-weight: 500;
    font-variant: small-caps;
    white-space: nowrap;
    line-height: 1;
  }
  .brand-name--front {
    left: 68px;
    top: 219px;
    font-size: 34px;
    color: var(--navy);
  }
  .brand-name--back {
    left: 428px;
    top: 172px;
    font-size: 56px;
    color: var(--card-white);
  }
  .holder {
    position: absolute;
    right: 52px;
    top: 88px;
    text-align: right;
    font-family: "Tinos", serif;
    font-weight: 700;
    color: var(--brand-blue);
  }
  .holder__name { font-size: 31px; line-height: 1.2; }
  .holder__role { font-size: 26px; line-height: 1.3; }
  .contact {
    position: absolute;
    left: 68px;
    top: 294px;
    margin: 0;
    padding: 0;
    list-style: none;
    font-family: "Open Sans", sans-serif;
    font-size: 22.5px;
    color: var(--ink);
  }
  .contact__item {
    display: flex;
    align-items: center;
    height: 34px;
  }
  .contact__icon {
    width: 20px;
    height: 20px;
    margin-right: 15px;
    flex: none;
  }
  .address {
    position: absolute;
    left: 69px;
    top: 459px;
    margin: 0;
    font-family: "Open Sans", sans-serif;
    font-style: normal;
    font-size: 22.5px;
    line-height: 31px;
    color: var(--card-white);
  }
  .web-address {
    position: absolute;
    left: 440px;
    top: 241px;
    font-family: "Open Sans", sans-serif;
    font-size: 21px;
    letter-spacing: 4.2px;
    color: var(--card-white);
  }
  .back-emblem {
    position: absolute;
    left: 40px;
    top: 70px;
  }
</style>
</head>
<body>
<main class="canvas">

  <section class="card card--front" aria-label="Business card front">
    <svg class="card__band" viewBox="0 0 929 530" aria-hidden="true">
      <rect x="0" y="448" width="929" height="82" fill="var(--brand-blue)"/>
      <path d="M929 460 L640 460 Q612 460 596 478 L548 530 L929 530 Z" fill="var(--platinum)"/>
    </svg>

    <svg class="brand-mark" width="150" height="150" viewBox="0 0 150 150" aria-hidden="true">
      <circle cx="75" cy="75" r="66" fill="none" stroke="var(--navy)" stroke-width="6"/>
    </svg>
    <div class="brand-name brand-name--front">Corvenne Jewelers</div>

    <div class="holder">
      <div class="holder__name">Marisol T Avery</div>
      <div class="holder__role">Partner</div>
    </div>

    <ul class="contact">
      <li class="contact__item">
        <svg class="contact__icon" viewBox="0 0 24 24" aria-hidden="true"><path fill="var(--brand-blue)" d="M6.6 2.5 9.4 6.6 7.6 8.6c1.1 2.9 3.4 5.3 6.3 6.5l2-1.8 4.1 2.8-1.6 3.9C11.2 19.5 3.6 12 3.2 4.1Z"/></svg>
        860 555 0148
      </li>
      <li class="contact__item">
        <svg class="contact__icon" viewBox="0 0 24 24" aria-hidden="true"><path fill="var(--brand-blue)" d="M6.6 2.5 9.4 6.6 7.6 8.6c1.1 2.9 3.4 5.3 6.3 6.5l2-1.8 4.1 2.8-1.6 3.9C11.2 19.5 3.6 12 3.2 4.1Z"/></svg>
        860 555 0193
      </li>
      <li class="contact__item">
        <svg class="contact__icon" viewBox="0 0 24 24" aria-hidden="true"><rect x="1" y="5" width="22" height="14" fill="var(--brand-blue)"/><path d="M1.5 5.5 12 13 22.5 5.5M1.5 18.5 9 11.5M22.5 18.5 15 11.5" stroke="#fff" stroke-width="1.6" fill="none"/></svg>
        marisol@corvennejewelers.com
      </li>
      <li class="contact__item">
        <svg class="contact__icon" viewBox="0 0 24 24" aria-hidden="true"><g fill="none" stroke="var(--brand-blue)" stroke-width="1.6"><circle cx="12" cy="12" r="10"/><ellipse cx="12" cy="12" rx="4.5" ry="10"/><path d="M2 12h20M4 6.5h16M4 17.5h16M12 2v20"/></g></svg>
        Corvennejewelers.com
      </li>
    </ul>

    <address class="address">47 Alder Lane, Westbrook,<br>Connecticut 06498</address>
  </section>

  <section class="card card--back" aria-label="Business card back">
    <svg class="back-emblem" width="380" height="420" viewBox="0 0 380 420" aria-hidden="true">
      <circle cx="190" cy="230" r="170" fill="none" stroke="var(--card-white)" stroke-width="16"/>
    </svg>
    <div class="brand-name brand-name--back">Corvenne Jewelers</div>
    <div class="web-address">www.corvennejewelers.com</div>
  </section>

</main>
</body>
</html>
```